School Hallway Magnetic Display Design for school values

I am looking for a someone to help me design a magnetic hallway display that will hang in the hallway of our small school. There are several elements, including 1. 6ft by 4ft designed magnetic bulletin board, 2. Magnets that will stick to the board. See attachment for which elements belong where. The display will be for our TAVRON program, which rewards students for demonstrating our school values. We want the display to be beautiful and interactive. We are also rebranding, so we want the design to align with our new fonts and colors. In the attached PDF is an outline of our new brand guidelines. Unfortunately, we don't have the color codes, but I'm hoping that you can match the colors listed. Attached are elements to be used on the board, but please use your creativity to make it more dynamic and visually appealing. For example, the star magnets could be another shape. The TAVRON magnets must remain the same. I've included two photos of boards at other schools that inspired this project.

Target Market(s)

School Community

Industry/Entity Type

Education

Requirements
Should not have
• School Logo

```html
<!DOCTYPE html>
<html lang="en">
<head>
<meta charset="utf-8">
<title>TAVRON at LHS – Hallway Values Display</title>
<link rel="stylesheet" href="https://fonts.googleapis.com/css2?family=Playfair+Display:wght@800;900&display=swap">
<style>
  :root {
    --backdrop: #646464;
    --board: #ffffff;
    --coral: #de8a75;
    --coral-light: #e9a190;
    --lilac: #bd9cc4;
    --lilac-light: #d4afdc;
    --sage: #d7dfb9;
    --sage-light: #ebf2cf;
    --sun: #fedb80;
    --sun-light: #f8e4b0;
    --sky: #aecde4;
    --sky-light: #c8e3f7;
    --ocean: #2b5b93;
    --ocean-light: #678bb3;
    --navy: #204f73;
    --shadow: rgba(0, 0, 0, 0.45);
  }
  * { margin: 0; padding: 0; box-sizing: border-box; }
  html, body { width: 1200px; height: 2336px; overflow: hidden; background: var(--backdrop); }
  .display { position: relative; width: 1200px; height: 2336px; font-family: "Playfair Display", Georgia, serif; }

  .board {
    position: absolute; left: 85px; top: 86px; width: 1030px; height: 687px;
    background: var(--board);
    box-shadow: 14px 16px 18px var(--shadow);
    overflow: hidden;
  }
  .board-ornament {
    position: absolute; left: 0; top: 0; width: 140px; height: 687px;
    background: linear-gradient(180deg, var(--sun) 0%, var(--navy) 30%, var(--navy) 55%, var(--sun) 72%, var(--navy) 100%);
    opacity: 0.9;
  }
  .board-title {
    position: absolute; left: 186px; top: 52px;
    font-weight: 900; font-size: 106px; line-height: 1; letter-spacing: -1px; white-space: nowrap;
  }
  .board-title .program { color: var(--coral); }
  .board-title .joiner { color: var(--lilac); }
  .board-title .school { color: var(--sky); }

  .value-magnet {
    position: absolute; left: 73px; width: 596px; height: 200px; border-radius: 100px;
    box-shadow: 12px 14px 16px var(--shadow); overflow: hidden;
  }
  .value-magnet .label {
    position: absolute; left: 34px; top: 0; height: 200px; line-height: 200px;
    font-weight: 900; font-size: 54px; color: #fff; letter-spacing: 0.5px; white-space: nowrap;
  }
  .value-magnet .sprig {
    position: absolute; left: 387px; top: 80px; width: 209px; height: 120px;
    border-radius: 60px 0 0 0; opacity: 0.85;
  }
  .simplicity { top: 853px; background: var(--coral); }
  .simplicity .sprig { background: var(--coral-light); }
  .peace { top: 1080px; background: var(--lilac); }
  .peace .sprig { background: var(--lilac-light); }
  .integrity { top: 1308px; background: var(--sage); }
  .integrity .sprig { background: var(--sage-light); }
  .community { top: 1535px; background: var(--sun); }
  .community .sprig { background: var(--sun-light); }
  .equality { top: 1762px; background: var(--sky); }
  .equality .sprig { background: var(--sky-light); }
  .stewardship { top: 1989px; background: var(--ocean); }
  .stewardship .sprig { background: var(--ocean-light); }

  .thermometer { position: absolute; left: 0; top: 0; width: 1200px; height: 2336px; filter: drop-shadow(12px 14px 10px var(--shadow)); }
  .thermometer .outline { fill: #fff; stroke: var(--navy); stroke-width: 7; }
  .thermometer .column { fill: none; stroke: var(--navy); stroke-width: 3.5; }
  .thermometer .tick { stroke: var(--navy); stroke-width: 2.5; }
</style>
</head>
<body>
<main class="display">
  <section class="board">
    <div class="board-ornament" role="img" aria-label="Decorative leaves and concentric sun circles in navy, yellow and coral"></div>
    <h1 class="board-title"><span class="program">TAVRON</span> <span class="joiner">at</span> <span class="school">LHS</span></h1>
  </section>

  <div class="value-magnet simplicity"><span class="label">Simplicity</span><div class="sprig" role="img" aria-label="Faint leaf motif"></div></div>
  <div class="value-magnet peace"><span class="label">Peace</span><div class="sprig" role="img" aria-label="Faint leaf motif"></div></div>
  <div class="value-magnet integrity"><span class="label">Integrity</span><div class="sprig" role="img" aria-label="Faint leaf motif"></div></div>
  <div class="value-magnet community"><span class="label">Community</span><div class="sprig" role="img" aria-label="Faint leaf motif"></div></div>
  <div class="value-magnet equality"><span class="label">Equality</span><div class="sprig" role="img" aria-label="Faint leaf motif"></div></div>
  <div class="value-magnet stewardship"><span class="label">Stewardship</span><div class="sprig" role="img" aria-label="Faint leaf motif"></div></div>

  <svg class="thermometer" viewBox="0 0 1200 2336" aria-label="Progress thermometer">
    <path class="outline" d="M830 1840 V1077 A81.5 81.5 0 0 1 993 1077 V1840 A172 172 0 1 1 830 1840 Z"/>
    <path class="column" d="M887 1878 V1075 A23.5 23.5 0 0 1 934 1075 V1878 A115 115 0 1 1 887 1878 Z"/>
    <g class="ticks">
      <line class="tick" x1="850" x2="886" y1="1202" y2="1202"/>
      <line class="tick" x1="850" x2="872" y1="1235" y2="1235"/>
      <line class="tick" x1="850" x2="872" y1="1268" y2="1268"/>
      <line class="tick" x1="850" x2="872" y1="1302" y2="1302"/>
      <line class="tick" x1="850" x2="886" y1="1335" y2="1335"/>
      <line class="tick" x1="850" x2="872" y1="1368" y2="1368"/>
      <line class="tick" x1="850" x2="872" y1="1401" y2="1401"/>
      <line class="tick" x1="850" x2="872" y1="1434" y2="1434"/>
      <line class="tick" x1="850" x2="886" y1="1468" y2="1468"/>
      <line class="tick" x1="850" x2="872" y1="1501" y2="1501"/>
      <line class="tick" x1="850" x2="872" y1="1534" y2="1534"/>
      <line class="tick" x1="850" x2="872" y1="1567" y2="1567"/>
      <line class="tick" x1="850" x2="886" y1="1600" y2="1600"/>
      <line class="tick" x1="850" x2="872" y1="1634" y2="1634"/>
      <line class="tick" x1="850" x2="872" y1="1667" y2="1667"/>
      <line class="tick" x1="850" x2="872" y1="1700" y2="1700"/>
      <line class="tick" x1="850" x2="886" y1="1733" y2="1733"/>
      <line class="tick" x1="850" x2="872" y1="1766" y2="1766"/>
      <line class="tick" x1="850" x2="872" y1="1799" y2="1799"/>
      <line class="tick" x1="850" x2="872" y1="1832" y2="1832"/>
    </g>
  </svg>
</main>
</body>
</html>
```